Lawn Sign For Construction Projects - Brisk Current

This contest is for a lawn sign that will be placed in the front yard of recently completed construction projects. The goal here is to have a bold advertising sign that is visible from a vehicle driving past.

We are still deciding on the default size for our sign, we also may use multiple sizes. The two sizes we will more than likely be using are: 18"h x 24"w and 24"h x 36"w.

Preference will be given to designers that submit original designs that tie into our current brand and are either in both the size formats listed above or are easy to scale in photoshop or illustrator.

In the files, you will see our logo and an example of a lawn sign.

Please contact us with any questions or comments you may have!

Thank You,
- The Brisk Current Team

Industry/Entity Type

Residential Construction

Colors
34a7d8
ffffff
faa54b

Requirements
Nice to have
• 1. The sign must tie into our current branding and color scheme.
• 2. The sign must be clearly visible and readable.
• 3. The sign must include our phone number in readable print.
• 4. Our website written in small print along the bottom of the sign.
• 5. Must mention we install the following products:
• a.) Solar
• b.) Roofing
• c.) Windows
• d.) Artificial Lawn
• e.) Whole House Fans
• f.) Patio Covers

```html
<!DOCTYPE html>
<html lang="en">
<head>
<meta charset="utf-8">
<title>Brisk Current – Lawn Sign</title>
<link rel="stylesheet" href="https://fonts.googleapis.com/css2?family=Archivo+Black&family=Questrial&display=swap">
<style>
  :root {
    --backdrop: #e8ebe7;
    --sign-black: #000000;
    --sun-yellow: #ffe600;
    --sun-gold: #ffc20e;
    --sun-amber: #f8a51c;
    --brand-orange: #ee7623;
    --brand-blue: #1273bd;
    --white: #ffffff;
  }
  html, body {
    margin: 0;
    padding: 0;
    width: 1200px;
    height: 1200px;
    overflow: hidden;
    background: var(--backdrop);
  }
  .lawn-sign {
    position: absolute;
    left: 50px;
    top: 187px;
    width: 1100px;
    height: 825px;
    display: block;
  }
  .brand-name {
    font-family: "Archivo Black", "Arial Black", sans-serif;
    font-size: 44px;
    fill: var(--brand-orange);
  }
  .brand-dot { fill: var(--brand-orange); }
  .headline {
    font-family: "Archivo Black", "Arial Black", sans-serif;
    font-size: 206px;
    fill: var(--brand-orange);
    stroke: var(--sign-black);
    stroke-width: 9px;
    stroke-linejoin: round;
    paint-order: stroke fill;
  }
  .phone {
    font-family: "Questrial", "Century Gothic", sans-serif;
    font-size: 112px;
    fill: var(--white);
  }
  .website {
    font-family: "Questrial", "Century Gothic", sans-serif;
    font-size: 40px;
    fill: var(--white);
  }
</style>
</head>
<body>
<svg class="lawn-sign" viewBox="0 0 1100 825" xmlns="http://www.w3.org/2000/svg">
  <defs>
    <radialGradient id="sunGlow" cx="540" cy="390" r="720" gradientUnits="userSpaceOnUse">
      <stop offset="0" stop-color="var(--sun-yellow)"/>
      <stop offset="0.55" stop-color="var(--sun-gold)"/>
      <stop offset="1" stop-color="var(--sun-amber)"/>
    </radialGradient>
  </defs>

  <rect class="sun-field" x="0" y="0" width="1100" height="600" fill="url(#sunGlow)"
        role="img" aria-label="Sunburst rays radiating from the top right corner"/>
  <polygon class="header-wedge" points="0,0 1100,0 0,253" fill="var(--sign-black)"/>

  <g class="brand">
    <circle class="brand-dot" cx="76" cy="84" r="26"/>
    <text class="brand-name" x="118" y="100">BRISK CURRENT</text>
  </g>

  <text class="headline" x="550" y="361" text-anchor="middle" textLength="594" lengthAdjust="spacingAndGlyphs">Local</text>
  <text class="headline" x="550" y="535" text-anchor="middle" textLength="849" lengthAdjust="spacingAndGlyphs">Experts</text>

  <rect class="contact-band" x="0" y="600" width="1100" height="225" fill="var(--brand-blue)"/>
  <text class="phone" x="550" y="716" text-anchor="middle" textLength="777" lengthAdjust="spacing">044 318 2605</text>
  <text class="website" x="550" y="783" text-anchor="middle">www.briskcurrent.example</text>
</svg>
</body>
</html>
```